Harbin Motors LLC

Car Dealer Customer Service
Address: 2847 Calloway Avenue, Shelbyville, TN 37160
web: www.harbinmotorsco.example
email: harbinmotorsco@mailbox.example
Phone: (931) 555-0147
Phone: (629) 555-0183

```html
<!DOCTYPE html>
<html lang="en">
<head>
<meta charset="utf-8">
<title>Harbin Motors – Business Card</title>
<link href="https://fonts.googleapis.com/css2?family=Montserrat:wght@500;600;800&display=swap" rel="stylesheet">
<style>
  :root {
    --backdrop: #b3b3b3;
    --card-light: #ffffff;
    --card-dark: #000000;
    --brand-blue: #1e7db3;
    --ink: #111111;
  }
  * { margin: 0; padding: 0; box-sizing: border-box; }
  html, body { width: 1000px; height: 1200px; overflow: hidden; }
  body {
    background: var(--backdrop);
    font-family: "Montserrat", sans-serif;
    position: relative;
  }
  .card {
    position: absolute;
    left: 50px;
    width: 900px;
    height: 540px;
  }
  .card--front { top: 43px; background: var(--card-light); }
  .card--back { top: 617px; background: var(--card-dark); }

  .brand-mark {
    position: absolute;
    border-radius: 50%;
    background: var(--brand-blue);
  }
  .brand-name {
    position: absolute;
    font-family: "Montserrat", sans-serif;
    font-weight: 800;
    color: var(--brand-blue);
    white-space: nowrap;
    letter-spacing: 0.5px;
  }
  .card--front .brand-mark { left: 170px; top: 50px; width: 150px; height: 150px; }
  .card--front .brand-name { left: 56px; top: 212px; font-size: 39px; }
  .card--back .brand-mark { left: 375px; top: 166px; width: 150px; height: 150px; }
  .card--back .brand-name { left: 0; width: 900px; text-align: center; top: 358px; font-size: 47px; }

  .service-title {
    position: absolute;
    left: 393px;
    top: 288px;
    font-size: 32px;
    font-weight: 500;
    color: var(--ink);
    white-space: nowrap;
  }
  .contact-list {
    position: absolute;
    left: 393px;
    top: 335px;
    list-style: none;
  }
  .contact-item {
    display: flex;
    align-items: center;
    height: 34px;
    font-size: 19.5px;
    font-weight: 500;
    color: var(--ink);
    white-space: nowrap;
  }
  .contact-icon {
    width: 22px;
    height: 22px;
    margin-right: 8px;
    flex: none;
    border-radius: 2px;
    background: var(--brand-blue);
  }
</style>
</head>
<body>
  <section class="card card--front">
    <div class="brand-mark"></div>
    <div class="brand-name">HARBIN MOTORS</div>

    <h1 class="service-title">Car Dealer Customer Service</h1>
    <ul class="contact-list">
      <li class="contact-item">
        <svg class="contact-icon" viewBox="0 0 22 22" aria-hidden="true">
          <path d="M11 4a4 4 0 0 0-4 4c0 3 4 8 4 8s4-5 4-8a4 4 0 0 0-4-4z" fill="none" stroke="#fff" stroke-width="1.5"/>
          <circle cx="11" cy="8" r="1.4" fill="#fff"/>
          <line x1="7" y1="18" x2="15" y2="18" stroke="#fff" stroke-width="1.5"/>
        </svg>
        2847 Calloway Avenue, Shelbyville, TN 37160
      </li>
      <li class="contact-item">
        <svg class="contact-icon" viewBox="0 0 22 22" aria-hidden="true">
          <g fill="none" stroke="#fff" stroke-width="1.2">
            <circle cx="11" cy="11" r="6"/>
            <ellipse cx="11" cy="11" rx="2.6" ry="6"/>
            <line x1="5" y1="11" x2="17" y2="11"/>
            <line x1="6" y1="8" x2="16" y2="8"/>
            <line x1="6" y1="14" x2="16" y2="14"/>
          </g>
        </svg>
        www.harbinmotorsco.example
      </li>
      <li class="contact-item">
        <svg class="contact-icon" viewBox="0 0 22 22" aria-hidden="true">
          <g fill="none" stroke="#fff" stroke-width="1.3">
            <rect x="4" y="6" width="14" height="10"/>
            <polyline points="4,6 11,12 18,6"/>
            <line x1="4" y1="16" x2="9" y2="11"/>
            <line x1="18" y1="16" x2="13" y2="11"/>
          </g>
        </svg>
        harbinmotorsco@mailbox.example
      </li>
      <li class="contact-item">
        <svg class="contact-icon" viewBox="0 0 22 22" aria-hidden="true">
          <path d="M7 5l2.5 0 1 3.5-1.6 1.2a8 8 0 0 0 3.4 3.4l1.2-1.6 3.5 1v2.5c0 .6-.5 1-1 1A11 11 0 0 1 6 6c0-.5.4-1 1-1z" fill="#fff"/>
        </svg>
        (931) 555-0147
      </li>
      <li class="contact-item">
        <svg class="contact-icon" viewBox="0 0 22 22" aria-hidden="true">
          <path d="M7 5l2.5 0 1 3.5-1.6 1.2a8 8 0 0 0 3.4 3.4l1.2-1.6 3.5 1v2.5c0 .6-.5 1-1 1A11 11 0 0 1 6 6c0-.5.4-1 1-1z" fill="#fff"/>
        </svg>
        (629) 555-0183
      </li>
    </ul>
  </section>

  <section class="card card--back">
    <div class="brand-mark"></div>
    <div class="brand-name">HARBIN MOTORS</div>
  </section>
</body>
</html>
```